Dental Specialist Needs a Business Card

We are a state of the art dental specialty office and need a business card that looks modern but professional.
I have provided our logo design in both vertical and horizontal. We use the design on letterhead in the vertical format but provided both forms for you. Thanks

Please add the address, phone and fax numbers I listed to all designs and please leave a space for website and for my employee name on each design. Thanks 2847 Halloway Avenue, Suite K East Marlow, NY 14391 Phone (716)382-9157 Fax:(716)382-9150 My name is Miles R.Dunford,D.D.S. If you want to show it with my name but the design needs to allow for the name to be switched.

Industry/Entity Type

Business

```html
<!DOCTYPE html>
<html lang="en">
<head>
<meta charset="utf-8">
<title>Keystone Endodontics – Business Card</title>
<link rel="stylesheet" href="https://fonts.googleapis.com/css2?family=Arimo:wght@400;700&family=Open+Sans:wght@400;700&display=swap">
<style>
  :root {
    --backdrop: #2e2c2a;
    --card: #ffffff;
    --leaf-green: #a6d157;
    --sky-blue: #86cdf3;
    --icon-blue: #22b0e6;
    --ink: #111111;
    --ink-soft: #555555;
    --rule: #8a8a8a;
  }
  * { margin: 0; padding: 0; box-sizing: border-box; }
  html, body {
    width: 1200px; height: 900px; overflow: hidden;
    background: var(--backdrop);
  }
  .business-card {
    position: absolute; left: 180px; top: 210px;
    width: 840px; height: 480px;
    background: var(--card);
    overflow: hidden;
    box-shadow: 0 10px 30px rgba(0,0,0,.45);
  }
  .accent-green {
    position: absolute; left: 0; top: 0;
    width: 320px; height: 240px;
    background: radial-gradient(ellipse at 0% 0%, var(--leaf-green) 0%, rgba(166,209,87,.55) 45%, rgba(166,209,87,0) 75%);
  }
  .accent-blue {
    position: absolute; right: 0; bottom: 0;
    width: 460px; height: 270px;
    background: radial-gradient(ellipse at 100% 100%, var(--sky-blue) 0%, rgba(134,205,243,.55) 45%, rgba(134,205,243,0) 75%);
  }
  .holder-name {
    position: absolute; left: 56px; top: 212px;
    font-family: "Open Sans", sans-serif;
  }
  .holder-name .name {
    font-weight: 700; font-size: 30px; color: var(--ink); line-height: 1.1;
  }
  .holder-name .credential {
    font-weight: 400; font-size: 26px; color: var(--ink-soft);
    letter-spacing: 1px; line-height: 1.1;
  }
  .divider {
    position: absolute; left: 402px; top: 292px;
    width: 2px; height: 150px; background: var(--rule);
  }
  .brand {
    position: absolute; left: 470px; top: 96px;
    display: flex; align-items: center; gap: 18px;
    font-family: "Arimo", sans-serif; color: var(--ink); font-weight: 400;
  }
  .brand .brand-dot {
    width: 56px; height: 56px; border-radius: 50%; background: var(--icon-blue);
  }
  .brand .brand-name { font-size: 42px; line-height: 1; letter-spacing: 1px; }
  .brand .brand-sub { font-size: 15px; letter-spacing: 4px; margin-top: 4px; }
  .contact-list {
    position: absolute; left: 440px; top: 300px;
    list-style: none;
    font-family: "Arimo", sans-serif; font-size: 19px; color: var(--ink);
  }
  .contact-list li {
    display: flex; align-items: flex-start; gap: 14px; margin-bottom: 10px;
    line-height: 1.2;
  }
  .contact-list svg { flex: none; width: 24px; height: 24px; }
  .contact-list .address { margin-bottom: 14px; }
</style>
</head>
<body>
<div class="business-card">
  <div class="accent-green" role="img" aria-label="Green decorative accent in the top-left corner"></div>
  <div class="accent-blue" role="img" aria-label="Light blue decorative accent in the bottom-right corner"></div>

  <div class="brand">
    <div class="brand-dot"></div>
    <div>
      <div class="brand-name">KEYSTONE</div>
      <div class="brand-sub">Endodontics P.C.</div>
    </div>
  </div>

  <div class="holder-name">
    <div class="name">Miles R.Dunford</div>
    <div class="credential">D.D.S</div>
  </div>

  <div class="divider"></div>

  <ul class="contact-list">
    <li class="address">
      <svg viewBox="0 0 24 24"><circle cx="12" cy="12" r="12" fill="var(--icon-blue)"/><path fill="#fff" d="M12 5a4.5 4.5 0 0 0-4.5 4.5c0 3.3 4.5 9 4.5 9s4.5-5.7 4.5-9A4.5 4.5 0 0 0 12 5zm0 6.2a1.7 1.7 0 1 1 0-3.4 1.7 1.7 0 0 1 0 3.4z"/></svg>
      <span>2847 Halloway Avenue, Suite K<br>East Marlow, NY 14391</span>
    </li>
    <li>
      <svg viewBox="0 0 24 24"><circle cx="12" cy="12" r="12" fill="var(--icon-blue)"/><path fill="#fff" d="M8.6 6.2l1.9 2.4-1.1 1.4c.8 1.7 2 2.9 3.7 3.7l1.4-1.1 2.4 1.9-.9 2c-4.6.2-9.5-4.7-9.3-9.3z"/></svg>
      <span>(716)382-9157</span>
    </li>
    <li>
      <svg viewBox="0 0 24 24"><circle cx="12" cy="12" r="12" fill="var(--icon-blue)"/><rect x="7" y="10" width="10" height="7" rx="1" fill="#fff"/><rect x="9" y="6" width="6" height="4" fill="#fff"/><rect x="9" y="12" width="6" height="1.4" fill="var(--icon-blue)"/></svg>
      <span>(716)382-9150</span>
    </li>
    <li>
      <svg viewBox="0 0 24 24"><circle cx="12" cy="12" r="12" fill="var(--icon-blue)"/><g fill="none" stroke="#fff" stroke-width="1.4"><circle cx="12" cy="12" r="6"/><ellipse cx="12" cy="12" rx="2.6" ry="6"/><path d="M6 12h12"/></g></svg>
      <span>www.keystoneendo.com</span>
    </li>
  </ul>
</div>
</body>
</html>
```